Facebook page as well as a business card and stationary design for a fitness instructor/personal trainer who is branching out as an independent worker delivering the gym experience (personal training or small group classes) to the home market. The trainer (LD or Lev Dunmore) is young, energetic, and results oriented.

Job Type
Facebook page and 2-sided business card
Task Outline
Create a Facebook presence (supported by a business card) for a train-you-at-home personal trainer
Task Description
Looking for a Graphic Designer/Web Designer to make a really modern/clean Facebook page that promotes Lev Dunmore ("LD") as at-your-home personal trainer. Lev's goal as a personal trainer is to motivate, inspire and educate all of his clients about the benefits of regular exercise, nourishing the body with nutritious foods, and living a healthy lifestyle while enjoying working out. He wants to encourage the convenience component of what he does by offering personal training sessions at a person's home or place of business. He trains both men and women, so the design of both the business card and the Facebook page should appeal to both genders and not come across as more feminine or more masculine. The Facebook page should include links to the Twitter, Instagram, and email accounts. It should also hold a placeholder link to his future web site called BougeAvecToi.

He holds several certifications and would like these mentioned on his Facebook page and perhaps on his business card -- either in text form or identifying them with the logos (which are attached).

Contact information for the business card will be supplied shortly. In the interim, the following can be used: Lev Dunmore Personal Trainer; Address: 47 Valmorin, Dollard-des-Ormeaux, Quebec, K7R 2P4, Email: ldstrongdaily@mailbox.example; Phone: 555.204-3917; Facebook: LDStrongDaily; Twitter: LDStrongDaily; Website: BougeAvecToi.example

OTHER INFORMATION: This project is a Christmas present to the personal trainer who is a friend. He'll be making the final decisions on the designs for both components.
Updates

Reason: I haven't given designers enough time to respond to my feedback. I apologize for any inconveniences. Best regard.

Target Market(s)

Both men and women who don't have the time for the gym and are looking for personal training at home or at their place of work.

Industry/Entity Type

Personal Trainer

Contact Information for Business Card

No photo. Clean lines and preference of blue colouring. contact information presented clearly. Card design must radiate the concept of fitness for life, living healthy and strong.

Font styles to use
Sans Serif

Colors
34a7d8
86cae6
85acd3
0355a3
0592ce
cee9f5
ceddec
86cfc6
cfeae6

```html
<!DOCTYPE html>
<html lang="fr">
<head>
<meta charset="utf-8">
<title>Bouge Avec Toi — Couverture</title>
<link rel="stylesheet" href="https://fonts.googleapis.com/css2?family=Arimo:wght@400&family=Libre+Baskerville:wght@700&display=swap">
<style>
  :root {
    --sky-pale: #eaf6fb;
    --sky-light: #cee9f5;
    --sky-mid: #86cae6;
    --sky-strong: #34a7d8;
    --ocean: #0592ce;
    --navy: #0355a3;
    --lime-tint: #cfe98a;
    --ink: #0d0d0d;
    --icon-blue: #5aaee0;
    --tagline: #2d8fd6;
  }
  html, body {
    margin: 0;
    padding: 0;
    width: 1200px;
    height: 444px;
    overflow: hidden;
    background: #ffffff;
  }
  .cover {
    position: relative;
    width: 1200px;
    height: 444px;
    overflow: hidden;
    font-family: "Arimo", Arial, sans-serif;
  }
  .cover-backdrop {
    position: absolute;
    inset: 0;
    width: 1200px;
    height: 444px;
  }
  .brand-name {
    position: absolute;
    left: 124px;
    top: 44px;
    margin: 0;
    font-family: "Libre Baskerville", Georgia, serif;
    font-weight: 700;
    font-size: 33px;
    letter-spacing: 0.5px;
    color: var(--ink);
    white-space: nowrap;
  }
  .services {
    list-style: none;
    margin: 0;
    padding: 0;
  }
  .services li {
    position: absolute;
    font-size: 24px;
    line-height: 1;
    color: var(--ink);
    white-space: nowrap;
  }
  .services .sport { left: 110px; top: 101px; }
  .services .food { left: 99px; top: 135px; }
  .services .weight { left: 93px; top: 168px; }
  .services .wellness { left: 87px; top: 202px; }

  .contact {
    position: absolute;
    right: 780px;
    top: 240px;
    text-align: right;
    color: var(--ink);
    line-height: 1;
  }
  .contact-label { font-size: 15px; margin-bottom: 8px; }
  .contact-phone { font-size: 21px; margin-bottom: 4px; }
  .contact-email { font-size: 18px; margin-bottom: 5px; }
  .contact-web { font-size: 18px; margin-right: 10px; }

  .pictogram {
    position: absolute;
    border-radius: 6px;
  }
  .pictogram-runner {
    left: 566px; top: 212px; width: 70px; height: 56px;
    background: linear-gradient(90deg, rgba(90,174,224,0.35), rgba(90,174,224,0.8));
  }
  .pictogram-dumbbell {
    left: 687px; top: 228px; width: 82px; height: 40px;
  }
  .pictogram-progress {
    left: 832px; top: 195px; width: 142px; height: 80px;
    background: linear-gradient(90deg, rgba(90,174,224,0.75), rgba(90,174,224,0.55));
  }
  .pictogram-stretch {
    left: 1008px; top: 193px; width: 86px; height: 85px;
    background: linear-gradient(90deg, rgba(90,174,224,0.7), rgba(90,174,224,0.5));
  }
  .tagline {
    position: absolute;
    left: 628px;
    top: 293px;
    margin: 0;
    font-size: 18px;
    color: var(--tagline);
    white-space: nowrap;
  }
</style>
</head>
<body>
<main class="cover">
  <svg class="cover-backdrop" viewBox="0 0 1200 444" aria-hidden="true">
    <defs>
      <linearGradient id="sky" x1="0" y1="0" x2="0" y2="1">
        <stop offset="0" stop-color="#8fd0ec"/>
        <stop offset="0.45" stop-color="#c3e6f4"/>
        <stop offset="0.72" stop-color="#eef8fc"/>
        <stop offset="1" stop-color="#9fd6ee"/>
      </linearGradient>
      <linearGradient id="panel" x1="0" y1="0" x2="1" y2="1">
        <stop offset="0" stop-color="#7ec4ea" stop-opacity="0.95"/>
        <stop offset="1" stop-color="#a9daf1" stop-opacity="0.85"/>
      </linearGradient>
      <linearGradient id="panel-deep" x1="0" y1="0" x2="1" y2="0">
        <stop offset="0" stop-color="#4fb0e2" stop-opacity="0.9"/>
        <stop offset="1" stop-color="#6cbfe8" stop-opacity="0.5"/>
      </linearGradient>
      <linearGradient id="glow" x1="0" y1="0" x2="0" y2="1">
        <stop offset="0" stop-color="#ffffff" stop-opacity="0"/>
        <stop offset="0.5" stop-color="#ffffff" stop-opacity="0.9"/>
        <stop offset="1" stop-color="#ffffff" stop-opacity="0"/>
      </linearGradient>
      <radialGradient id="corner" cx="0" cy="0" r="1">
        <stop offset="0" stop-color="#cfe98a"/>
        <stop offset="1" stop-color="#cfe98a" stop-opacity="0"/>
      </radialGradient>
    </defs>
    <rect width="1200" height="444" fill="url(#sky)"/>
    <polygon points="640,0 1200,0 1200,120 760,190" fill="#ffffff" opacity="0.22"/>
    <polygon points="900,0 1200,0 1200,60" fill="#ffffff" opacity="0.3"/>
    <rect x="0" y="330" width="1200" height="80" fill="url(#glow)"/>
    <polygon points="0,0 545,0 430,444 0,444" fill="url(#panel)"/>
    <polygon points="0,0 150,0 60,444 0,444" fill="url(#panel-deep)"/>
    <polygon points="260,0 545,0 470,290 360,140" fill="#ffffff" opacity="0.18"/>
    <polygon points="0,340 420,380 430,444 0,444" fill="#ffffff" opacity="0.25"/>
    <rect width="140" height="130" fill="url(#corner)"/>
  </svg>

  <h1 class="brand-name">Bouge Avec Toi</h1>

  <ul class="services">
    <li class="sport">SPORT</li>
    <li class="food">ALIMENTATION</li>
    <li class="weight">PERTE DE POIDS</li>
    <li class="wellness">BIEN-ÊTRE</li>
  </ul>

  <address class="contact" style="font-style: normal;">
    <div class="contact-label">Contact me :</div>
    <div class="contact-phone">555.204-3917</div>
    <div class="contact-email">ldstrongdaily@mailbox.example</div>
    <div class="contact-web">www.bougeavectoi.example</div>
  </address>

  <div class="pictogram pictogram-runner" role="img" aria-label="Pictogramme d'un coureur en pleine course"></div>
  <svg class="pictogram pictogram-dumbbell" viewBox="0 0 82 40" role="img" aria-label="Haltère">
    <rect x="0" y="14" width="6" height="12" rx="2" fill="var(--icon-blue)"/>
    <rect x="9" y="4" width="9" height="32" rx="3" fill="var(--icon-blue)"/>
    <rect x="18" y="17" width="46" height="6" fill="var(--icon-blue)"/>
    <rect x="64" y="4" width="9" height="32" rx="3" fill="var(--icon-blue)"/>
    <rect x="76" y="14" width="6" height="12" rx="2" fill="var(--icon-blue)"/>
  </svg>
  <div class="pictogram pictogram-progress" role="img" aria-label="Silhouettes montrant la progression de la perte de poids"></div>
  <div class="pictogram pictogram-stretch" role="img" aria-label="Silhouettes de personnes faisant des étirements"></div>

  <p class="tagline">Méthode et conseils pour perdre du poids</p>
</main>
</body>
</html>
```